KOR Methodology infographic that shows flow of the process outlined on our web site

We are looking for a graphical representation of the methodology that is described on this web page: https://www.kor-example.com/about-kor/methodology/ We would like someone to be able to quickly understand our methodology and the key points outlined on the web page - the graphic should be able to do that.

Target Market(s)

Enterprise Companies with 1000+ employees

Industry/Entity Type

Information Technology

Font styles to use
Sans Serif

Colors
3277b5
abd036
faa54b

Requirements
Must have
• Must convey the method/process with enough detail to understand what the process is.
Nice to have
• Arrows or something showing flow would be great
Should not have
• Should not be "cartoony"

```html
<!DOCTYPE html>
<html lang="en">
<head>
<meta charset="utf-8">
<title>KOR – Our Methodology</title>
<link href="https://fonts.googleapis.com/css2?family=Roboto:wght@400;500;700&display=swap" rel="stylesheet">
<style>
  :root{
    --page:#2b2b2b;
    --sheet:#f3f7ec;
    --navy:#10295a;
    --blue:#3277b5;
    --green:#abd036;
    --orange:#faa54b;
    --red:#ec4f3b;
    --ring:#e4e6e3;
    --line:#9aa3ad;
  }
  *{margin:0;padding:0;box-sizing:border-box}
  html,body{width:1200px;height:1200px;overflow:hidden;background:var(--page)}
  body{font-family:'Roboto',sans-serif;color:var(--navy);position:relative}
  .sheet{position:absolute;left:0;top:134px;width:1200px;height:932px;background:var(--sheet)}
  .title{position:absolute;left:0;right:0;top:18px;text-align:center;font-weight:700;font-size:40px;letter-spacing:.5px}
  .title span{border-bottom:2px solid var(--navy);padding-bottom:2px}
  .brand{position:absolute;right:60px;top:30px;display:flex;align-items:center;gap:8px;font-weight:700;font-size:38px;color:var(--navy)}
  .brand i{display:block;width:22px;height:22px;border-radius:50%;background:var(--green)}
  .intro{position:absolute;left:100px;right:100px;top:132px;text-align:center;font-size:15.5px;line-height:20px}
  .note{position:absolute;width:232px;height:138px;border-radius:6px;color:#fff;font-size:11.2px;line-height:13.4px;text-align:center;display:flex;align-items:center;justify-content:center;padding:10px 12px}
  .note--assess{left:109px;top:237px;background:var(--blue)}
  .note--consult{left:109px;top:531px;background:#a4c93a}
  .note--develop{left:861px;top:237px;background:var(--orange)}
  .note--implement{left:861px;top:531px;background:var(--red)}
  .connectors{position:absolute;left:0;top:0;width:1200px;height:932px}
  .wheel{position:absolute;left:344px;top:210px;width:511px;height:511px}
  .seg-label{fill:#fff;font-weight:500;font-size:9.5px;text-anchor:middle}
  .seg-num{fill:#fff;font-weight:500;font-size:10.5px;text-anchor:middle}
  .wheel-word{fill:var(--navy);font-weight:700;font-size:22px;letter-spacing:1px}
  .closing{position:absolute;left:109px;right:100px;top:783px;font-size:15.5px;line-height:20px}
  .closing p+p{margin-top:13px}
</style>
</head>
<body>
<main class="sheet">
  <h1 class="title"><span>OUR METHODOLOGY</span></h1>
  <div class="brand"><i></i>KOR</div>

  <p class="intro">KOR has a longstanding belief in committing to the client throughout the sales, planning, and deployment processes. More than two decades and thousands of engagements later, KOR has created distinctive methodology guidelines for a successful project.</p>

  <svg class="connectors" viewBox="0 0 1200 932" aria-hidden="true">
    <g stroke="var(--line)" stroke-width="1" fill="none">
      <polyline points="341,306 372,306 394,340"/>
      <polyline points="859,306 828,306 806,340"/>
      <polyline points="341,599 366,599 384,576"/>
      <polyline points="857,601 832,601 812,576"/>
    </g>
    <circle cx="341" cy="306" r="4" fill="var(--blue)"/>
    <circle cx="859" cy="306" r="4" fill="var(--blue)"/>
    <circle cx="341" cy="599" r="4" fill="var(--green)"/>
    <circle cx="857" cy="601" r="4" fill="var(--green)"/>
  </svg>

  <div class="note note--assess">Very often after an initial consultation is over, the process is best served by adding an assessment phase. This process can range from simple interviews to full enterprise evaluations. The assessment stage should end with the discovery of all pertinent information needed for the development of an effective solution.</div>
  <div class="note note--consult">A first conversation in any relationship is vitally important. This is especially true when beginning an IT project. Setting expectations and defining success are integral parts of the process. An initial consultation with KOR will be filled with questions and listening as we discover the concerns you have and consider the best approach to help you achieve your goals.</div>
  <div class="note note--develop">Your KOR team includes members of the account management, engineering, and finance departments. After initial consultations and assessments are completed, your team convenes to design and draw up solutions for your consideration.</div>
  <div class="note note--implement">Upon acceptance of a quote and a subsequent purchase order, the certified KOR engineers proceed with your implementation.</div>

  <svg class="wheel" viewBox="-200 -200 400 400" role="img" aria-label="Four-step methodology wheel: initial consultation, assessment, solution development, implementation">
    <defs>
      <path id="word-arc" d="M -86,128 A 154 154 0 0 0 99,118"/>
    </defs>
    <circle r="188" fill="#fff" stroke="var(--ring)" stroke-width="4"/>
    <!-- outer band -->
    <path d="M -149,-86 A172 172 0 0 1 0,-172 L0,-78 A78 78 0 0 0 -67.5,-39 Z" fill="var(--blue)"/>
    <path d="M 0,-172 A172 172 0 0 1 161.6,-58.8 L73.3,-26.7 A78 78 0 0 0 0,-78 Z" fill="var(--orange)"/>
    <path d="M 161.6,-58.8 A172 172 0 0 1 110.6,131.8 L50.1,59.7 A78 78 0 0 0 73.3,-26.7 Z" fill="var(--red)"/>
    <path d="M -96.2,142.6 A172 172 0 0 1 -149,-86 L-67.5,-39 A78 78 0 0 0 -43.6,64.7 Z" fill="var(--green)"/>
    <!-- inner band -->
    <path d="M -55.4,-32 A64 64 0 0 1 0,-64 L0,-38 A38 38 0 0 0 -32.9,-19 Z" fill="var(--blue)"/>
    <path d="M 0,-64 A64 64 0 0 1 60.1,-21.9 L35.7,-13 A38 38 0 0 0 0,-38 Z" fill="var(--orange)"/>
    <path d="M 60.1,-21.9 A64 64 0 0 1 41.1,49 L24.4,29.1 A38 38 0 0 0 35.7,-13 Z" fill="var(--red)"/>
    <path d="M -35.8,53.1 A64 64 0 0 1 -55.4,-32 L-32.9,-19 A38 38 0 0 0 -21.2,31.5 Z" fill="var(--green)"/>
    <circle r="72" fill="none" stroke="#fff" stroke-width="10"/>
    <circle r="38" fill="#fff" stroke="var(--ring)" stroke-width="2"/>
    <!-- flow arrows -->
    <g fill="none" stroke="rgba(0,0,0,.22)" stroke-width="4" stroke-linecap="round">
      <path d="M -28,-135 Q -10,-145 8,-138"/>
      <path d="M 108,-62 Q 120,-48 118,-32"/>
      <path d="M 98,95 Q 92,110 80,118"/>
      <path d="M -118,20 Q -122,4 -116,-12"/>
    </g>
    <g fill="rgba(0,0,0,.22)">
      <polygon points="6,-145 16,-137 5,-131"/>
      <polygon points="111,-34 125,-34 118,-24"/>
      <polygon points="84,125 74,114 86,112"/>
      <polygon points="-122,-10 -110,-10 -116,-20"/>
    </g>
    <text class="seg-label" x="-71" y="-100">ASSESSMENT</text>
    <text class="seg-label" x="72" y="-104">SOLUTION</text>
    <text class="seg-label" x="72" y="-92">DEVELOPMENT</text>
    <text class="seg-label" x="126" y="24">IMPLEMENTATION</text>
    <text class="seg-label" x="-124" y="38">INITIAL</text>
    <text class="seg-label" x="-124" y="50">CONSULTATION</text>
    <text class="seg-num" x="-27" y="-39">02</text>
    <text class="seg-num" x="34" y="-35">03</text>
    <text class="seg-num" x="50" y="19">04</text>
    <text class="seg-num" x="-50" y="15">01</text>
    <circle cx="-20" cy="0" r="4" fill="var(--green)"/>
    <text x="6" y="5" text-anchor="middle" font-weight="700" font-size="15" fill="var(--navy)">KOR</text>
    <text class="wheel-word"><textPath href="#word-arc" startOffset="50%" text-anchor="middle">METHODOLOGY</textPath></text>
  </svg>

  <div class="closing">
    <p>Proper integration and testing ensures that no delays or unexpected problems will occur. Business units stay on schedule and commitments are met. Success is only achieved when all expectations are satisfied.</p>
    <p>No matter what your industry is, KOR can help you build and customize your technology needs and support them with services provided by the finest certified engineers in the business.</p>
  </div>
</main>
</body>
</html>
```